New management consulting website

I need a 4-5 page website that I can manage in WordPress on Hostlane.example for a new management consulting company. The website is www.torvik-example.com and the company name is Torvik Group LLC. The attached spec has an example of a draft site, layout and actual copy and includes company and contact information. I have more high-res images I can send.

Must include instruction/assistance loading the site to my WordPress dashboard.

Target Market(s)

Any business, especially SAAS

Industry/Entity Type

Consultant

Coding

Coded - Design and coding required

Number of Pages Required

4 page

Font styles to use
Sans Serif

Colors
0456a4

Requirements
Must have
• Modern and stylish

```html
<!DOCTYPE html>
<html lang="en">
<head>
<meta charset="utf-8">
<title>Torvik Consulting</title>
<link href="https://fonts.googleapis.com/css2?family=Michroma&family=Montserrat:wght@400;500;600&display=swap" rel="stylesheet">
<style>
:root{
  --brand:#0456a4;
  --brand-dark:#0a4794;
  --ink:#1b1b1b;
  --muted:#7a7a7a;
  --white:#ffffff;
  --black:#000000;
  --display:"Michroma",sans-serif;
  --body:"Montserrat",sans-serif;
}
*{margin:0;padding:0;box-sizing:border-box}
html,body{width:1200px;height:3759px;overflow:hidden}
body{position:relative;background:var(--white);font-family:var(--body);color:var(--ink)}
.abs{position:absolute}
/* header */
.site-header{left:0;top:0;width:1200px;height:86px;background:var(--white)}
.brand{left:99px;top:14px;text-align:center;font-family:var(--body);font-weight:600;color:#223f6b}
.brand .name{font-size:44px;letter-spacing:2px;line-height:46px}
.brand .tag{font-size:14px;letter-spacing:1px;color:#777;line-height:14px}
.nav{right:99px;top:36px;display:flex;gap:43px;font-size:14px;letter-spacing:.3px}
.nav a{color:var(--ink);text-decoration:none}
.nav a.active{color:var(--brand)}
/* hero */
.hero{left:0;top:86px;width:1200px;height:629px;background:linear-gradient(100deg,#e9dccf 0%,#a9b7c6 35%,#6c849c 60%,#1a2430 78%,#050505 100%)}
.hero-title{left:101px;top:255px;font-family:var(--display);font-size:60px;line-height:64px;color:var(--ink)}
.hero-text{left:102px;top:410px;width:560px;font-size:19px;line-height:29px;font-weight:500;text-align:justify}
.dots{left:517px;top:672px;display:flex;gap:12px}
.dots span{width:47px;height:3px;background:var(--white)}
.dots span.on{background:var(--brand)}
/* about */
.h2{font-family:var(--display);font-size:34px;color:var(--ink);line-height:40px}
.about-copy{left:98px;top:915px;width:441px;font-size:13.5px;line-height:24px;color:var(--muted);text-align:justify}
.about-copy p+p{margin-top:24px}
.btn{left:98px;top:1168px;width:184px;height:55px;border-radius:28px;background:var(--brand);color:var(--white);font-size:15px;display:flex;align-items:center;justify-content:center}
.photo{display:block}
/* services */
.tile{width:327px;height:340px;overflow:hidden}
.tile .label{position:absolute;left:16px;bottom:12px;color:var(--white);font-weight:600;font-size:22px;letter-spacing:.5px}
.tile-feature{background:var(--brand);color:var(--white);padding:42px 20px 0 17px}
.tile-feature h3{font-weight:600;font-size:21px;margin-bottom:12px}
.tile-feature p{font-size:14px;line-height:24.8px;text-align:justify}
/* team */
.team{left:0;top:2174px;width:1200px;height:588px;background:linear-gradient(180deg,var(--brand-dark),#0d4c9c)}
.frame{left:150px;top:2313px;width:378px;height:341px;background:var(--white)}
.team-copy{left:615px;top:2330px;width:461px;color:var(--white)}
.team-copy .h2{color:var(--white)}
.team-copy .who{font-weight:600;font-size:19px;margin-top:8px}
.team-copy .role{font-size:13px;opacity:.85;margin-top:2px}
.team-copy p{font-size:13.5px;line-height:24px;text-align:justify;margin-top:20px}
/* origins */
.origins-title{left:0;top:2878px;width:1200px;text-align:center}
.origins-sub{left:0;top:2928px;width:1200px;text-align:center;font-size:13.5px;color:var(--muted)}
/* footer */
.footer{left:0;top:3314px;width:1200px;height:445px;background:var(--black);color:var(--white)}
.footer .brand{left:99px;top:66px;color:var(--white)}
.footer .brand .tag{color:var(--white)}
.social{left:99px;top:162px;width:18px;height:18px;background:var(--white)}
.col{top:78px}
.col h4{font-weight:500;font-size:19px;margin-bottom:24px}
.col li{list-style:none;font-size:14px;line-height:24.7px}
.copyright{left:0;top:404px;width:1200px;text-align:center;font-size:11px}
</style>
</head>
<body>

<header class="abs site-header">
  <div class="abs brand"><div class="name">TORVIK</div><div class="tag">CONSULTING</div></div>
  <nav class="abs nav">
    <a class="active" href="#">HOME</a><a href="#">ABOUT US</a><a href="#">SERVICES</a><a href="#">TEAM</a><a href="#">BLOG</a><a href="#">CONTACT US</a>
  </nav>
</header>

<section class="abs hero" role="img" aria-label="Misty blue mountain ranges with two climbers silhouetted on a dark cliff, one helping the other up"></section>
<h1 class="abs hero-title">TORVIK<br>CONSULTING</h1>
<p class="abs hero-text">Lorem ipsum dolor sit amet, consectetur adipiscing elit, sed do eiusmod tempor incididunt ut labore et dolore magna aliqua. Ut enim ad minim veniam</p>
<div class="abs dots"><span class="on"></span><span></span><span></span></div>

<h2 class="abs h2" style="left:98px;top:842px">ABOVE &amp; BEYOND</h2>
<div class="abs about-copy">
  <p>Lorem ipsum dolor sit amet, consectetur adipiscing elit, sed do eiusmod tempor incididunt ut labore et dolore magna aliqua. Ut enim ad minim veniam, quis nostrud exercitation ullamco laboris nisi ut aliquip ex ea commodo consequat.</p>
  <p>Duis aute irure dolor in reprehenderit in voluptate velit esse cillum dolore eu fugiat nulla pariatur. Excepteur sint occaecat cupidatat non proident, sunt in culpa qui officia deserunt mollit anim id est laborum.</p>
</div>
<div class="abs btn">Read More</div>
<div class="abs photo" style="left:636px;top:839px;width:466px;height:94px;background:linear-gradient(160deg,#9fb6d6,#2c63ad 45%,#0b3f8f)" role="img" aria-label="Bright blue sky with sun flare"></div>
<div class="abs photo" style="left:636px;top:988px;width:466px;height:244px;background:linear-gradient(180deg,#c99a4a,#e3b565 30%,#5a4632 65%,#1d1a17)" role="img" aria-label="Two people cheering on a mountain summit at sunset"></div>
<div class="abs" style="left:739px;top:1083px;width:363px;height:56px;background:var(--white)"></div>

<div class="abs tile" style="left:98px;top:1356px;background:linear-gradient(150deg,#cfcac4,#9a948d 60%,#6e6b68)" role="img" aria-label="Team members pointing at strategy charts on a table"><span class="label">Strategy &amp; Operations</span></div>
<div class="abs tile tile-feature" style="left:437px;top:1356px">
  <h3>Data Analysis &amp; Insights</h3>
  <p>Lorem ipsum dolor sit amet, consectetur adipiscing elit, sed do eiusmod tempor incididunt ut labore et dolore magna aliqua. Ut enim ad minim veniam, quis nostrud exercitation ullamco laboris nisi ut aliquip ex ea commodo consequat. Duis aute irure dolor in reprehenderit in voluptate velit esse cillum dolore eu fugiat nulla pariatur.</p>
</div>
<h2 class="abs h2" style="left:825px;top:1485px;font-size:36px;line-height:42px">OUR<br>SERVICES</h2>
<div class="abs tile" style="left:98px;top:1710px;background:linear-gradient(160deg,#8a4a35,#b9a99a 50%,#4d4a48)" role="img" aria-label="Colleagues in a meeting around a table against a brick wall"><span class="label">Leadership Development</span></div>
<div class="abs tile" style="left:437px;top:1710px;background:linear-gradient(160deg,#f3b25a,#c96b2a 45%,#3d2a22)" role="img" aria-label="Speaker addressing an audience in front of tall sunlit windows"><span class="label">Executive Leadership</span></div>
<div class="abs tile" style="left:775px;top:1710px;background:linear-gradient(180deg,#2f7ad0,#8eb7d8 45%,#f0d24a 70%,#1a1a1a)" role="img" aria-label="Silhouettes of people helping each other climb a cliff at sunset"><span class="label">Torvik Consulting</span></div>

<section class="abs team"></section>
<div class="abs frame"></div>
<div class="abs photo" style="left:166px;top:2298px;width:377px;height:342px;background:linear-gradient(150deg,#d8d4cf,#b9b2aa)" role="img" aria-label="Portrait of Elias Marrow, founder"></div>
<div class="abs team-copy">
  <h2 class="h2">OUR TEAM</h2>
  <div class="who">Elias Marrow</div>
  <div class="role">Founder &amp; Senior Consultant</div>
  <p>Lorem ipsum dolor sit amet, consectetur adipiscing elit, sed do eiusmod tempor incididunt ut labore et dolore magna aliqua. Ut enim ad minim veniam, quis nostrud exercitation ullamco laboris nisi ut aliquip ex ea commodo consequat. Duis aute irure dolor in reprehenderit in voluptate velit esse cillum dolore eu fugiat nulla pariatur. Excepteur sint occaecat cupidatat non proident, sunt in culpa qui officia deserunt mollit anim id est laborum.</p>
</div>

<h2 class="abs h2 origins-title">THE ORIGINS OF TORVIK</h2>
<p class="abs origins-sub">Lorem ipsum dolor sit amet, consectetur adipiscing elit, sed do eiusmod tempor incididunt ut labore et dolore magna aliqua.</p>
<div class="abs photo" style="left:158px;top:2967px;width:292px;height:223px;background:linear-gradient(180deg,#3c5a3a,#6f7d60 50%,#3a3a3c)" role="img" aria-label="Straight road through a green forest"></div>
<div class="abs photo" style="left:454px;top:2967px;width:292px;height:223px;background:linear-gradient(180deg,#8fb7e0,#e6eef6 35%,#1d3566 80%)" role="img" aria-label="Darts hitting targets against a bright sky"></div>
<div class="abs photo" style="left:750px;top:2967px;width:292px;height:223px;background:linear-gradient(180deg,#8a7d6a,#c8a671 45%,#2a2420)" role="img" aria-label="Climber scaling a rock inside a businessman silhouette"></div>

<footer class="abs footer">
  <div class="abs brand"><div class="name">TORVIK</div><div class="tag">CONSULTING</div></div>
  <div class="abs social" role="img" aria-label="Professional network profile"></div>
  <div class="abs col" style="left:445px"><h4>Links</h4><ul><li>Home</li><li>About Us</li><li>Services</li><li>Team</li><li>Blog</li><li>Contact Us</li></ul></div>
  <div class="abs col" style="left:661px"><h4>Connect</h4><ul><li>CSR Initiatives</li><li>Read Articles</li><li>Media Kit</li><li>Employee Portal</li><li>Customer Portal</li><li>Offices</li><li>Know More</li></ul></div>
  <div class="abs col" style="left:889px"><h4>Contact Us</h4><ul><li>Address: 48 Larchmont Row</li><li>#210, Fairview, GA 30099</li><li>&nbsp;</li><li>Email: info@torvik-example.com</li><li>Tel: 555-014-0187</li></ul></div>
  <p class="abs copyright">© Copyrights.2021.The Company Name.All Rights Reserved</p>
</footer>

</body>
</html>
```